New Banner Ad Design Project

We are a start-up in San Francisco that sells consignment clothes with a percentage of the proceeds donated to charity. Also, volunteer groups can conduct dress drives and send them to us and we will sell them and give their charity back 60% of the proceeds.

We have several uses for banners:
- Home page banner:
- Promote timely Flash Sales (they last only 96 hours) which happen 2x/week
- Promote how good it feels to give back and shop
- Promote any special promotions such as a Gift With Purchase
- Community banner:
- Promote the lifestyle
- Promote any particular group conducting a dress drive

If you are going to submit one banner it is to be for an upcoming sale, as the two attached files address (maternity sale). If we find the right designer we will consider working with them beyond the design contest for future sale banners as well as others

We consider our 'competitors' to be The Garment Harbor, The TrueLoop, WovaSpin, KnitPeak, GlowAgain. Our key differentiator is the charitable components and how groups are conducting dress drives to raise money.

We are in the midst of changing our company name, tagline and logo. The new company will be called 'TessaLume' and our tagline is 'Restitched Kindness'

Target Market(s)

Our initial audience is young women 16 - 30. We will be focusing on Prom February through May which appeals to 16 - 18 year olds.

We also have maternity-wear. We want these women to feel fashionable

We are focused on individuals who want to give back.

Industry/Entity Type

Charity

Font styles to use
Serif
Sans Serif

Colors
8769ae
1b1b1b
474747
c3c3c3
86cfc6
b7a5cd

Requirements
Must have
• - Youthful and stylish voice (not to be confused with Young)
- Appealing visuals
- Powerful call-to-action as it pertains to banners for our flash sales
- An inclusive feel
- Communicates our charitable component
Nice to have
• - Emotional appeal
- Women wearing our clothes (see attached)
Should not have
• - Too much text
- Too girly; overly flowery

```html
<!DOCTYPE html>
<html lang="en">
<head>
<meta charset="UTF-8">
<title>TessaLume – Maternity Sale Banner</title>
<link rel="stylesheet" href="https://fonts.googleapis.com/css2?family=Montserrat:wght@300;400;800&family=Raleway:wght@200;300;400&display=swap">
<style>
  :root {
    --autumn-deep: #6b2c0c;
    --autumn-rust: #b4501a;
    --autumn-orange: #e08a22;
    --autumn-gold: #f2c53a;
    --path-warm: #c9652a;
    --portrait-tone: #9a8e86;
    --portrait-shade: #5b524e;
    --ribbon-purple: #6d4f8f;
    --ribbon-edge: #574075;
    --tag-red: #e5342f;
    --tag-red-dark: #b9221f;
    --string: #f4efe9;
    --text-light: #ffffff;
  }
  * { margin: 0; padding: 0; box-sizing: border-box; }
  html, body {
    width: 1200px; height: 400px; overflow: hidden; background: #ffffff;
  }
  .banner {
    position: relative; width: 1200px; height: 400px; overflow: hidden;
    font-family: "Montserrat", Arial, sans-serif; color: var(--text-light);
  }
  .scene {
    position: absolute; inset: 0;
    background:
      radial-gradient(ellipse 420px 260px at 1080px 170px, var(--autumn-gold) 0%, rgba(242,197,58,0) 100%),
      radial-gradient(ellipse 500px 220px at 520px 60px, var(--autumn-orange) 0%, rgba(224,138,34,0) 100%),
      linear-gradient(180deg, var(--autumn-rust) 0%, var(--autumn-deep) 55%, var(--path-warm) 100%);
  }
  .portrait {
    position: absolute; left: 820px; top: 0; width: 220px; height: 400px;
    border-radius: 100px 100px 0 0;
    background: linear-gradient(180deg, var(--portrait-tone) 0%, var(--portrait-shade) 100%);
  }
  .brand {
    position: absolute; left: 60px; top: 40px; width: 500px; text-align: center;
  }
  .brand-name {
    font-family: "Raleway", Arial, sans-serif; font-weight: 300;
    font-size: 60px; letter-spacing: 9px; line-height: 1;
  }
  .brand-tagline {
    font-family: "Raleway", Arial, sans-serif; font-weight: 400;
    font-size: 19px; letter-spacing: 6px; margin-top: 10px;
  }
  .offer {
    position: absolute; left: 160px; top: 150px; width: 340px; text-align: center;
    font-size: 38px; line-height: 1.0; text-shadow: 0 2px 4px rgba(0,0,0,0.45);
  }
  .offer strong { font-weight: 800; }
  .offer span { font-weight: 300; }
  .offer-line + .offer-line { margin-top: 4px; }
  .sale-graphics { position: absolute; left: 0; top: 0; }
  .sale-title {
    position: absolute; left: 200px; top: 302px;
    font-family: "Raleway", Arial, sans-serif; font-weight: 300;
    font-size: 48px; letter-spacing: 1px; line-height: 52px; white-space: nowrap;
  }
  .discount-tag {
    position: absolute; left: 64px; top: 296px; width: 120px;
    transform: rotate(24deg); text-align: center;
    font-family: "Montserrat", Arial, sans-serif; font-weight: 800;
    line-height: 1.05;
  }
  .discount-tag .amount { font-size: 16px; }
  .discount-tag .word { font-size: 16px; }
</style>
</head>
<body>
  <div class="banner">
    <div class="scene" role="img" aria-label="Autumn park avenue lined with golden-orange trees and fallen leaves"></div>

    <div class="portrait" role="img" aria-label="Pregnant woman wearing a patterned short-sleeved maternity dress with a black sash"></div>

    <div class="brand">
      <div class="brand-name">TESSALUME</div>
      <div class="brand-tagline">RESTITCHED KINDNESS</div>
    </div>

    <div class="offer">
      <div class="offer-line"><strong>MORE</strong> <span>ITEMS!</span></div>
      <div class="offer-line"><strong>BIGGER</strong> <span>SAVINGS!</span></div>
    </div>

    <svg class="sale-graphics" width="1200" height="400" viewBox="0 0 1200 400" aria-hidden="true">
      <path d="M0 250 Q 40 262 78 300" fill="none" stroke="var(--string)" stroke-width="2"/>
      <polygon points="70,298 548,298 522,329 548,360 70,360" fill="var(--ribbon-purple)"/>
      <line x1="70" y1="360" x2="548" y2="360" stroke="var(--ribbon-edge)" stroke-width="2"/>
      <g transform="rotate(24 124 326)">
        <polygon points="78,300 186,300 186,352 78,352 60,326" fill="var(--tag-red)"/>
        <polygon points="78,352 186,352 186,356 78,356" fill="var(--tag-red-dark)"/>
        <circle cx="76" cy="326" r="4" fill="var(--string)"/>
      </g>
    </svg>

    <div class="discount-tag">
      <div class="amount">UP TO 80%</div>
      <div class="word">OFF</div>
    </div>

    <div class="sale-title">MATERNITY SALE</div>
  </div>
</body>
</html>
```